Dietitian needs a new business card design

I need a new business card design for my nutrition business that provides individual clinical nutrition advice for people with medical conditions. Business cards will be handed out to doctors, specialists and clients so will need to be sharp and project an image of professionalism

Target Market(s)

My clients are typically referred by doctors or specialists and the card will be used to handout to clients and their doctors.

Industry/Entity Type

Medical

Contact Information for Business Card

The business card will require the details below. These details can be found from my website https://www.kelvarrowclinic.com.au/

Font styles to use
Serif

Colors

Designer to choose colors to be used in the design.

Requirements
Must have
• 1. It needs be professional and contemporary
• 2. It needs to incorporate my logo
• 3. It needs space to write appointment times and dates
• 4. It needs to provide my phone number, fax number, email address and my web address
Nice to have
• Include the Registered Tovance Clinician Logo
• I have access to Framellow if required
• The locations I practise from
Should not have
• Pictures of food
• Spelling MIstakes

```html
<!DOCTYPE html>
<html lang="en">
<head>
<meta charset="utf-8">
<title>Kelvarrow Nutrition – Business Card</title>
<link rel="stylesheet" href="https://fonts.googleapis.com/css2?family=Gentium+Book+Plus:wght@400;700&display=swap">
<style>
  :root{
    --page:#e7e4df;
    --card:#ffffff;
    --brand-blue:#2a3f8f;
    --rule-teal:#2bb3c8;
    --green-light:#c9e46a;
    --green:#8cc63f;
    --green-dark:#5a9a22;
    --orange:#f2a23a;
    --ink:#3a3a3a;
    --ink-soft:#5c5c5c;
    --name-grey:#6b6b6b;
  }
  *{box-sizing:border-box;margin:0;padding:0}
  html,body{width:1200px;height:1023px;overflow:hidden}
  body{background:var(--page);font-family:"Gentium Book Plus",Georgia,serif;color:var(--ink);position:relative}

  .card{position:absolute;left:220px;width:760px;height:420px;background:var(--card);
    box-shadow:0 6px 18px rgba(0,0,0,.18);overflow:hidden}
  .card--front{top:50px}
  .card--back{top:540px;background:linear-gradient(160deg,#ffffff 40%,#ececec 100%)}

  /* front */
  .brand{position:absolute;left:36px;top:44px;display:flex;align-items:center;gap:14px}
  .brand__dot{width:46px;height:46px;border-radius:50%;background:var(--brand-blue)}
  .brand__name{font-size:52px;color:var(--brand-blue);line-height:1}

  .badge{position:absolute;right:0;top:0;width:196px;height:128px;background:var(--green-light);
    padding:18px 20px}
  .badge__panel{width:100%;height:100%;background:var(--orange);display:flex;align-items:center;gap:10px;padding:0 12px}
  .badge__label{color:#fff;font-size:12.5px;line-height:1.25;flex:1}
  .badge__seal{width:44px;height:44px;border-radius:50%;background:#fff;flex:none}

  .locations{position:absolute;left:36px;top:150px;display:grid;grid-template-columns:repeat(4,1fr);
    gap:18px;width:560px;font-size:11.5px;line-height:1.35;color:var(--ink-soft)}

  .divider{position:absolute;left:0;top:258px;width:100%;height:5px;
    background:linear-gradient(90deg,var(--brand-blue),var(--rule-teal) 50%,var(--brand-blue))}
  .band{position:absolute;left:0;top:263px;width:100%;height:157px;
    background:radial-gradient(ellipse at 40% 40%,var(--green-light),var(--green) 60%,var(--green-dark))}
  .person{position:absolute;left:36px;top:22px}
  .person__name{font-size:34px;color:var(--name-grey);letter-spacing:.5px}
  .person__role{font-size:16px;color:var(--name-grey);margin-top:8px;line-height:1.5;padding-left:40px}
  .contacts{position:absolute;left:410px;top:26px;border-left:1.5px solid #3e5a1a;padding-left:18px;
    list-style:none;font-size:15px;color:#243a0c;line-height:1.75}
  .contacts li{display:flex;align-items:center;gap:9px}
  .contacts svg{width:15px;height:15px;flex:none}

  /* back */
  .back-brand{position:absolute;right:40px;top:44px;display:flex;align-items:center;gap:12px}
  .appointment{position:absolute;left:60px;top:118px;width:430px}
  .appointment__kicker{font-size:13px;letter-spacing:2px;color:var(--ink)}
  .appointment__title{font-size:32px;letter-spacing:2px;color:#222;margin-top:2px}
  .field{display:flex;align-items:flex-end;gap:16px;margin-top:52px;font-size:26px;letter-spacing:2px;color:#222}
  .field__line{flex:1;border-bottom:1.5px solid #444;height:26px}
</style>
</head>
<body>

<section class="card card--front" aria-label="Business card front">
  <div class="brand">
    <span class="brand__dot"></span>
    <span class="brand__name">Kelvarrow Nutrition</span>
  </div>

  <div class="badge">
    <div class="badge__panel">
      <span class="badge__label">Registered Tovance Clinician</span>
      <span class="badge__seal"></span>
    </div>
  </div>

  <div class="locations">
    <p>Brindlemoor Medical Centre<br>Cnr Hale &amp; Marlow Streets<br>Ashcombe<br>Halvern Tasmania<br>7250<br>brindlemoormedical.com.au</p>
    <p>Fenwick Medical<br>3/118 Orrin Road<br>Fenwick Tasmania<br>7250</p>
    <p>Cleave Valley Health<br>4 Harrow Drive<br>Riverbend Tasmania<br>7250<br>cleavevalleyhealth.com.au</p>
    <p>Tallis Doctors Surgery<br>9 Corbin Road<br>Tallis Tasmania<br>tallisdoctors.com.au</p>
  </div>

  <div class="divider"></div>

  <div class="band">
    <div class="person">
      <p class="person__name">Adrian Pellworth</p>
      <p class="person__role">Accredited Nutritionist<br>Qualified Chef</p>
    </div>
    <ul class="contacts">
      <li><svg viewBox="0 0 16 16"><path fill="#2a3f8f" d="M4 1l3 3-2 2c1 2 3 4 5 5l2-2 3 3-2 3C7 15 1 9 1 3z"/></svg>0400 555 217</li>
      <li><svg viewBox="0 0 16 16"><rect x="3" y="1" width="9" height="5" fill="#2a3f8f"/><rect x="1" y="6" width="14" height="8" rx="1" fill="#2a3f8f"/><rect x="4" y="9" width="8" height="2" fill="#fff"/></svg>+613 5550 0147</li>
      <li><svg viewBox="0 0 16 16"><rect x="1" y="3" width="14" height="10" fill="#2a3f8f"/><path d="M1 3l7 6 7-6" stroke="#fff" fill="none"/></svg>adrian@kelvarrowclinic.com.au</li>
      <li><svg viewBox="0 0 16 16" fill="none" stroke="#2a3f8f" stroke-width="1.4"><circle cx="8" cy="8" r="6.5"/><ellipse cx="8" cy="8" rx="3" ry="6.5"/><path d="M1.5 8h13"/></svg>https://www.kelvarrowclinic.com.au/</li>
    </ul>
  </div>
</section>

<section class="card card--back" aria-label="Business card back">
  <div class="back-brand">
    <span class="brand__dot"></span>
    <span class="brand__name" style="font-size:40px">Kelvarrow Nutrition</span>
  </div>

  <div class="appointment">
    <p class="appointment__kicker">YOUR NEXT</p>
    <p class="appointment__title">APPOINTMENT :</p>
    <div class="field"><span>DATE</span><span class="field__line"></span></div>
    <div class="field"><span>TIME</span><span class="field__line"></span></div>
  </div>
</section>

</body>
</html>
```